Need Label for Our Jams Product

HI,

we have are launching a new brand in the premium foods category by the name of Vo-Pantry. the logo has been designed and our first product is Premium 65% fruit Jams. we need a label for it now. can you help ?

our flavours are strawberry, apple, mango, blackberry, cherry, PineApple.

Please note that we need one design and then we will modify it according to the flavour. so you will need to make one flavour on a theme. and then we will apply the theme accordingly to the rest of the flavours.

Target Market(s)

Health concious people who donot want to use ordinary jams any further.

Industry/Entity Type

Product

Requirements
Must have
• the logo, not too big because we need the flavour name aswell on the front of the label.
also would appreciate a touch of fruit or similar
also please note that the colour of the cap in the attached picture is the actual colour. and the label should incline with the colour of cap aswell. im not saying the label to be in that colour, but must balance the whole look of the bottle.
Please note that this is a round bottle, so much information is needed on the front. the sides of the labels will be occupied by ingredients nutrition facts etc.
Nice to have
• white background but not necessary.
Should not have
• black colour

```html
<!DOCTYPE html>
<html lang="en">
<head>
<meta charset="utf-8">
<title>Vo-Pantry Mango Jam Label</title>
<link href="https://fonts.googleapis.com/css2?family=Ubuntu:wght@400;700&family=Inconsolata:wght@400&family=Archivo+Narrow:wght@400;700&family=Alfa+Slab+One&display=swap" rel="stylesheet">
<style>
  :root {
    --sun-yellow: #fdc40f;
    --mango-orange: #f7941d;
    --flavour-orange: #f0a342;
    --leaf-green: #6b9a35;
    --ink: #3a3a3a;
    --paper: #ffffff;
    --panel-grey: #bdbdbd;
    --rule: #1f1f1f;
  }
  * { box-sizing: border-box; margin: 0; padding: 0; }
  html, body { width: 1200px; height: 257px; overflow: hidden; background: var(--paper); }
  .label { position: relative; width: 1200px; height: 257px; background: var(--paper); overflow: hidden; }

  /* side panel */
  .side-panel { position: absolute; left: 0; top: 0; width: 340px; height: 257px; background: var(--sun-yellow); }
  .band { position: absolute; top: 0; height: 257px; }
  .band--orange { left: 349px; width: 18px; background: var(--mango-orange); }
  .band--green { left: 376px; width: 14px; background: var(--leaf-green); }
  .band--orange-right { left: 987px; width: 11px; background: var(--mango-orange); }

  /* nutrition facts */
  .nutrition {
    position: absolute; left: 50px; top: 20px; width: 116px; height: 218px;
    background: var(--paper); border: 1px solid var(--rule); padding: 3px 4px;
    font-family: "Archivo Narrow", Arial, sans-serif; color: var(--rule); font-size: 5px; line-height: 1.25;
  }
  .nutrition__title { font-weight: 700; font-size: 13px; line-height: 1; letter-spacing: -0.2px; }
  .nutrition__bar { height: 4px; background: var(--rule); margin: 1px 0; }
  .nutrition__row { display: flex; justify-content: space-between; border-top: 0.5px solid var(--rule); padding: 0.5px 1px; }
  .nutrition__row--shade { background: var(--panel-grey); }
  .nutrition__row--indent { padding-left: 5px; }
  .nutrition__row strong { font-weight: 700; }
  .nutrition__note { font-size: 4px; line-height: 1.2; margin-top: 2px; }
  .nutrition__grid { display: grid; grid-template-columns: 2.1fr 1.2fr 1fr 1fr; font-size: 3.8px; line-height: 1.3; margin-top: 2px; }

  /* ingredients */
  .ingredients { position: absolute; left: 193px; top: 40px; }
  .ingredients__heading { font-family: "Ubuntu", sans-serif; font-size: 15px; color: var(--leaf-green); margin-bottom: 8px; }
  .ingredients__list { list-style: none; font-family: "Inconsolata", monospace; font-size: 13.5px; line-height: 14.5px; color: var(--ink); }

  /* front */
  .brand { position: absolute; left: 415px; top: 8px; text-align: center; }
  .brand__name { font-family: "Ubuntu", sans-serif; font-weight: 400; font-size: 24px; color: var(--leaf-green); line-height: 1; }
  .brand__tagline { font-family: "Ubuntu", sans-serif; font-size: 5px; letter-spacing: 1.6px; color: var(--leaf-green); margin-top: 1px; }
  .flavour-name { position: absolute; left: 406px; top: 40px; overflow: visible; }
  .flavour-name text { font-family: "Alfa Slab One", Georgia, serif; font-size: 128px; fill: var(--flavour-orange); }
  .product-type { position: absolute; left: 866px; top: 148px; font-family: "Ubuntu", sans-serif; font-weight: 700; font-size: 41px; color: var(--leaf-green); line-height: 1; letter-spacing: 1px; }
  .fruit-photo { position: absolute; left: 1002px; top: 0; }
</style>
</head>
<body>
<div class="label">
  <section class="side-panel">
    <div class="nutrition">
      <div class="nutrition__title">Nutrition Facts</div>
      <div>Serving Size 1 cup (228g)</div>
      <div>Servings Per Container 2</div>
      <div class="nutrition__bar"></div>
      <div style="font-size:4px">Amount Per Serving</div>
      <div class="nutrition__row"><span><strong>Calories</strong> 250</span><span>Calories from Fat 110</span></div>
      <div class="nutrition__row" style="justify-content:flex-end"><span>% Daily Value*</span></div>
      <div class="nutrition__row nutrition__row--shade"><span><strong>Total Fat</strong> 12g</span><span>18%</span></div>
      <div class="nutrition__row nutrition__row--shade nutrition__row--indent"><span>Saturated Fat 3g</span><span>15%</span></div>
      <div class="nutrition__row nutrition__row--indent"><span><em>Trans</em> Fat 1.5g</span><span></span></div>
      <div class="nutrition__row nutrition__row--shade"><span><strong>Cholesterol</strong> 30mg</span><span>10%</span></div>
      <div class="nutrition__row nutrition__row--shade"><span><strong>Sodium</strong> 470mg</span><span>20%</span></div>
      <div class="nutrition__row"><span><strong>Total Carbohydrate</strong> 31g</span><span>10%</span></div>
      <div class="nutrition__row nutrition__row--shade nutrition__row--indent"><span>Dietary Fiber 0g</span><span>0%</span></div>
      <div class="nutrition__row nutrition__row--indent"><span>Sugars 5g</span><span></span></div>
      <div class="nutrition__row"><span><strong>Protein</strong> 5g</span><span></span></div>
      <div class="nutrition__bar"></div>
      <div class="nutrition__row nutrition__row--shade"><span>Vitamin A</span><span>4%</span></div>
      <div class="nutrition__row nutrition__row--shade"><span>Vitamin C</span><span>2%</span></div>
      <div class="nutrition__row nutrition__row--shade"><span>Calcium</span><span>20%</span></div>
      <div class="nutrition__row nutrition__row--shade"><span>Iron</span><span>4%</span></div>
      <div class="nutrition__note">* Percent Daily Values are based on a 2,000 calorie diet. Your Daily Values may be higher or lower depending on your calorie needs.</div>
      <div class="nutrition__grid">
        <span></span><span>Calories</span><span>2,000</span><span>2,500</span>
        <span>Total Fat</span><span>Less than</span><span>65g</span><span>80g</span>
        <span>&nbsp;Sat Fat</span><span>Less than</span><span>20g</span><span>25g</span>
        <span>Cholesterol</span><span>Less than</span><span>300mg</span><span>300mg</span>
        <span>Sodium</span><span>Less than</span><span>2,400mg</span><span>2,400mg</span>
        <span>Total Carbohydrate</span><span></span><span>300g</span><span>375g</span>
        <span>&nbsp;Dietary Fiber</span><span></span><span>25g</span><span>30g</span>
      </div>
    </div>
    <div class="ingredients">
      <h2 class="ingredients__heading">Ingredients</h2>
      <ul class="ingredients__list">
        <li>fresh mango</li>
        <li>sugar</li>
        <li>fruit pectin</li>
        <li>natural flavors</li>
      </ul>
    </div>
  </section>

  <div class="band band--orange"></div>
  <div class="band band--green"></div>

  <header class="brand">
    <div class="brand__name">Vo-Pantry</div>
    <div class="brand__tagline">purely the finest fruit</div>
  </header>

  <svg class="flavour-name" width="575" height="160" viewBox="0 0 575 160" aria-label="mango">
    <text x="2" y="96" textLength="568" lengthAdjust="spacing">mango</text>
  </svg>

  <div class="product-type">JAM</div>

  <div class="band band--orange-right"></div>

  <svg class="fruit-photo" width="198" height="257" viewBox="0 0 198 257" role="img" aria-label="Photograph of ripe whole and sliced mangoes">
    <defs>
      <radialGradient id="mango-tone" cx="0.6" cy="0.35" r="0.8">
        <stop offset="0" stop-color="#ffb347"/>
        <stop offset="0.55" stop-color="#f7931e"/>
        <stop offset="1" stop-color="#e8611a"/>
      </radialGradient>
    </defs>
    <rect width="198" height="257" fill="url(#mango-tone)"/>
  </svg>
</div>
</body>
</html>
```